Business Card - Rebranding for Consulting Firm

We are renaming and rebranding our consulting firm and need to raise the level of quality of our cards as part of that effort. We consult to leading high tech, life science and other innovation sector companies.

Need a two-sided business card design.

Side 1: (a) Company logo (b) tag line: Optimize Your Investment in Talent (c) Name (d) Title (e) Phone 1: Office (f) Phone 2: Mobile (g) email: person@HollowmereAdvisory.com

Side 2: Two lines of text: (a) Markets Shift Fast. Teams Must Adapt. People Turn Plans into Results. (b) We guide you through every stage.

Target Market(s)

Business and human resources executives and senior managers

Industry/Entity Type

Management Consulting

Contact Information for Business Card

Font styles to use
Sans Serif

Requirements
Must have
• clean, not too busy, but with a bit of creativity. Stick to the colors used in the attached logo
• appeal to high tech, life science companies
Nice to have
• prefer white background

```html
<!DOCTYPE html>
<html lang="en">
<head>
<meta charset="utf-8">
<title>Hollowmere Advisory – Business Card</title>
<link href="https://fonts.googleapis.com/css2?family=Arimo:wght@400;700&display=swap" rel="stylesheet">
<style>
  :root{
    --bg:#dcdcdc;
    --card:#f6f6f6;
    --navy:#1a5f99;
    --blue:#2a8fd0;
    --sky:#3aa4e4;
    --faint:#c9d3e3;
    --ink:#1d3e66;
    --rule:#6f7f93;
  }
  *{box-sizing:border-box;margin:0;padding:0}
  html,body{width:1200px;height:900px;overflow:hidden}
  body{
    background:var(--bg);
    font-family:"Arimo",Arial,sans-serif;
    display:flex;align-items:center;justify-content:center;gap:60px;
  }
  .card{
    position:relative;width:540px;height:310px;background:var(--card);
    box-shadow:0 2px 6px rgba(0,0,0,.12);overflow:hidden;
  }
  /* Side 2 */
  .card--back .edge{position:absolute;top:0;left:0;right:0;height:9px;background:var(--sky)}
  .card--back .brand-faint{
    position:absolute;top:92px;left:0;right:0;text-align:center;color:var(--faint);
  }
  .brand-faint .brand-name{font-size:38px;font-weight:400;letter-spacing:-.5px}
  .brand-faint .brand-tag{font-size:13px;margin-top:4px}
  .card--back .band{
    position:absolute;left:0;right:0;bottom:0;height:66px;background:var(--navy);
    display:flex;flex-direction:column;justify-content:center;align-items:center;gap:4px;
  }
  .band .statement{color:#fff;font-size:12.5px}
  .band .promise{color:var(--sky);font-size:13px;font-weight:700}
  /* Side 1 */
  .card--front .brand{position:absolute;top:40px;right:40px;text-align:right}
  .brand .mark{display:inline-block;width:14px;height:14px;background:var(--navy);margin-right:8px;vertical-align:middle}
  .brand .brand-name{color:var(--navy);font-size:26px;font-weight:400;vertical-align:middle}
  .brand .brand-tag{color:var(--blue);font-size:11px;margin-top:6px}
  .person{position:absolute;right:40px;top:148px;text-align:right;padding-right:10px}
  .person::after{content:"";position:absolute;right:0;top:6px;width:2px;height:42px;background:var(--rule)}
  .person .name{font-size:20px;color:var(--blue)}
  .person .name b{color:var(--navy)}
  .person .title{font-size:11px;color:var(--ink);margin-top:2px}
  .contacts{position:absolute;left:28px;right:28px;bottom:26px;display:flex;justify-content:space-between;list-style:none}
  .contacts li{display:flex;align-items:center;gap:6px;font-size:10px;color:var(--blue)}
  .contacts svg{width:18px;height:18px}
</style>
</head>
<body>
  <section class="card card--back" aria-label="Card back">
    <div class="edge"></div>
    <div class="brand-faint">
      <div class="brand-name">Hollowmere Advisory LLC</div>
      <div class="brand-tag">“Invest Wisely in Your People.”</div>
    </div>
    <div class="band">
      <p class="statement">Markets Shift Fast. Teams Must Adapt. People Turn Plans into Results.</p>
      <p class="promise">“We guide you through every stage.”</p>
    </div>
  </section>

  <section class="card card--front" aria-label="Card front">
    <div class="brand">
      <span class="mark"></span><span class="brand-name">Hollowmere Advisory LLC</span>
      <p class="brand-tag">“Invest Wisely in Your People.”</p>
    </div>
    <div class="person">
      <p class="name"><b>Name</b> Surname</p>
      <p class="title">Managing Director</p>
    </div>
    <ul class="contacts">
      <li>
        <svg viewBox="0 0 20 20" aria-hidden="true"><circle cx="10" cy="10" r="9" fill="none" stroke="#1a5f99" stroke-width="1.5"/><path d="M6 8c0-1 1-2 4-2s4 1 4 2l-1 1h-1.5V8h-3v1H7zM6.5 10h7v4h-7z" fill="#1a5f99"/></svg>
        079-24810376
      </li>
      <li>
        <svg viewBox="0 0 20 20" aria-hidden="true"><circle cx="10" cy="10" r="9" fill="none" stroke="#1a5f99" stroke-width="1.5"/><rect x="7" y="4.5" width="6" height="11" rx="1" fill="none" stroke="#1a5f99" stroke-width="1.3"/><rect x="8.2" y="6" width="3.6" height="5" fill="#1a5f99"/></svg>
        +91-7812094563
      </li>
      <li>
        <svg viewBox="0 0 20 20" aria-hidden="true"><circle cx="10" cy="10" r="9" fill="none" stroke="#1a5f99" stroke-width="1.5"/><rect x="5" y="6.5" width="10" height="7" fill="none" stroke="#1a5f99" stroke-width="1.3"/><path d="M5 6.5l5 4 5-4" fill="none" stroke="#1a5f99" stroke-width="1.3"/></svg>
        person@HollowmereAdvisory.com
      </li>
    </ul>
  </section>
</body>
</html>
```